New label for Beauty Item - Quartz Willow

I am looking for a new, fresh and colorful design for my line of beauty products. Looking to be more modern and chic. Would like colors from the actual logo incorporated along with some type of flowers (lotus). Please take inspiration from the logo. Most labels are about 2x3.75 inches on a 1 ounce bottle. Must have room on label for ingredients, brief sales pitch and directions of use. You can see examples of products at www.myquartzwillow-example.com

Really like the design attached of flowers at the bottom (or shadow in the background), maybe have them as a lotus flower? Kinda of a more contemporary flower design instead of the real thing.

Target Market(s)

25-55 year old women primarily

Industry/Entity Type

Sales

```html
<!DOCTYPE html>
<html lang="en">
<head>
<meta charset="utf-8">
<title>Quartz Willow – Radiant Dew Labels</title>
<link rel="stylesheet" href="https://fonts.googleapis.com/css2?family=Oswald:wght@300;400&family=Lato:wght@400;700&display=swap">
<style>
  :root {
    --page: #eeeeee;
    --label: #ffffff;
    --ink: #1c1c1c;
    --brand-blue: #2b5f9e;
    --magenta: #d6338f;
    --lime: #7cc63a;
    --cyan: #2ba7de;
    --petal-green: #6fd25a;
    --petal-blue: #3550c9;
    --petal-pink: #e2447e;
  }
  * { box-sizing: border-box; margin: 0; padding: 0; }
  html, body { width: 1200px; height: 1106px; overflow: hidden; }
  body {
    background: var(--page);
    font-family: "Lato", sans-serif;
    color: var(--ink);
  }
  .label-row {
    position: absolute;
    top: 233px;
    left: 50px;
    display: flex;
    gap: 40px;
  }
  .label {
    position: relative;
    width: 340px;
    height: 640px;
    background: var(--label);
    box-shadow: 0 2px 10px rgba(0,0,0,0.08);
    display: flex;
    flex-direction: column;
    align-items: center;
    padding-top: 40px;
    overflow: hidden;
  }
  .brand {
    display: flex;
    flex-direction: column;
    align-items: center;
    gap: 8px;
  }
  .brand-dot {
    width: 58px;
    height: 58px;
    border-radius: 50%;
    background: var(--brand-blue);
  }
  .brand-name {
    font-family: "Lato", sans-serif;
    font-weight: 400;
    font-size: 28px;
    color: var(--brand-blue);
  }
  .product-name {
    margin-top: 8px;
    font-family: "Oswald", sans-serif;
    font-weight: 400;
    font-size: 56px;
    line-height: 0.95;
    text-align: center;
    letter-spacing: 1px;
    text-transform: uppercase;
  }
  .ribbon {
    margin-top: 12px;
    width: 280px;
    padding: 6px 0;
    color: #fff;
    font-size: 20px;
    text-align: center;
    clip-path: polygon(0 0, 100% 0, 96% 50%, 100% 100%, 0 100%, 4% 50%);
  }
  .tagline {
    margin-top: 14px;
    font-size: 14px;
    font-weight: 700;
  }
  .lotus {
    position: absolute;
    left: 20px;
    right: 20px;
    bottom: 40px;
    height: 250px;
    border-radius: 50% 50% 40% 40% / 70% 70% 30% 30%;
    opacity: 0.75;
  }
  .volume {
    position: absolute;
    bottom: 22px;
    right: 40px;
    font-size: 15px;
    color: #333;
  }
  .label--green .ribbon { background: var(--magenta); }
  .label--green .lotus { background: radial-gradient(ellipse at 50% 80%, var(--petal-green), rgba(111,210,90,0.15) 75%); }
  .label--blue .ribbon { background: var(--lime); }
  .label--blue .lotus { background: radial-gradient(ellipse at 50% 80%, var(--petal-blue), rgba(53,80,201,0.15) 75%); }
  .label--pink .ribbon { background: var(--cyan); }
  .label--pink .lotus { background: radial-gradient(ellipse at 50% 80%, var(--petal-pink), rgba(226,68,126,0.15) 75%); }
</style>
</head>
<body>
  <main class="label-row">
    <section class="label label--green">
      <div class="brand"><span class="brand-dot"></span><span class="brand-name">Quartz Willow</span></div>
      <h1 class="product-name">Radiant<br>Dew</h1>
      <p class="ribbon">50% Glycolic Acid Peel</p>
      <p class="tagline">Dermatologist Grade Glycolic Acid</p>
      <div class="lotus" role="img" aria-label="Stylised green lotus flower illustration"></div>
      <p class="volume">1 fluid oz</p>
    </section>
    <section class="label label--blue">
      <div class="brand"><span class="brand-dot"></span><span class="brand-name">Quartz Willow</span></div>
      <h1 class="product-name">Radiant<br>Dew</h1>
      <p class="ribbon">50% Glycolic Acid Peel</p>
      <p class="tagline">Dermatologist Grade Glycolic Acid</p>
      <div class="lotus" role="img" aria-label="Stylised blue lotus flower illustration"></div>
      <p class="volume">1 fluid oz</p>
    </section>
    <section class="label label--pink">
      <div class="brand"><span class="brand-dot"></span><span class="brand-name">Quartz Willow</span></div>
      <h1 class="product-name">Radiant<br>Dew</h1>
      <p class="ribbon">50% Glycolic Acid Peel</p>
      <p class="tagline">Dermatologist Grade Glycolic Acid</p>
      <div class="lotus" role="img" aria-label="Stylised pink lotus flower illustration"></div>
      <p class="volume">1 fluid oz</p>
    </section>
  </main>
</body>
</html>
```